Büro Vermietung
Velbrin Design Studio hat eine super Arbeit abgeliefert. Wir sind sehr zufrieden mit der Arbeit und natürlich mit dem Design.
Zielgruppe
Bitte keine weiteren Vorschläge mehr. - Wir haben uns bereits für ein Projekte entschieden.
Aufgabenstellung
Interessenten, welche sich für die Büros oder Gewerbefläche interessieren, sollten auf der Webpage folgende Informationen vorfinden:
Menü-Leiste:
HOME / FLÄCHEN / BILDER / LAGE / KONTAKT
HOME:
Titelbild mit dem Hund & weitblick-raeume.ch + Frontbild Liegenschaft
(Zusatztext folgt noch)
FLAECHEN:
Grundriss & Preise
BILDER:
diverse Bilder (folgen noch)
LAGE:
KONTAKT:
(Unsere Adresse) Vermieter /Kontakt
KARELU IMMOBILEN AG

```html
<!DOCTYPE html>
<html lang="de">
<head>
<meta charset="utf-8">
<title>Flächen – weitblick-raeume.ch</title>
<link rel="stylesheet" href="https://fonts.googleapis.com/css2?family=Open+Sans:wght@400;600;700&family=Short+Stack&display=swap">
<style>
  :root {
    --brand-red: #cc0528;
    --brand-red-dark: #a9031f;
    --ink-purple: #4e4a86;
    --text: #333333;
    --label: #2c2c2c;
    --white: #ffffff;
  }
  * { margin: 0; padding: 0; box-sizing: border-box; }
  html, body { width: 1200px; height: 823px; overflow: hidden; background: var(--white); }
  body { position: relative; font-family: "Open Sans", Verdana, sans-serif; color: var(--text); }

  .mascot {
    position: absolute; left: 112px; top: 0; width: 282px; height: 178px; z-index: 3;
    background: radial-gradient(ellipse at 45% 40%, #c98a4e 0%, #e8d6c2 45%, rgba(255,255,255,0) 72%);
  }
  .site-name {
    position: absolute; left: 291px; top: 64px; z-index: 4;
    font-family: "Short Stack", cursive; font-size: 28px; color: var(--ink-purple);
  }

  .nav-band { position: absolute; left: 0; top: 114px; width: 1200px; height: 38px; background: var(--brand-red); }
  .main-nav { position: absolute; left: 0; top: 114px; height: 38px; display: flex; z-index: 2; }
  .main-nav a {
    position: absolute; top: 0; height: 38px; line-height: 38px; transform: translateX(-50%);
    color: var(--white); text-decoration: none; font-size: 15px; padding: 0 10px; white-space: nowrap;
  }
  .main-nav a.is-active { background: var(--brand-red-dark); font-weight: 700; }

  .hero-photo {
    position: absolute; left: 0; top: 154px; width: 1200px; height: 197px;
    background: linear-gradient(90deg, #dfe3e3 0%, #c8d98a 30%, #e6e8e6 55%, #c3d47b 70%, #d9dcdc 100%);
  }
  .hero-fade {
    position: absolute; left: 0; top: 352px; width: 1200px; height: 24px;
    background: linear-gradient(#e2e4e2, #ffffff);
  }

  .content { position: absolute; left: 149px; top: 388px; width: 580px; }
  .page-title { font-family: "Short Stack", cursive; font-weight: 400; font-size: 31px; color: var(--ink-purple); line-height: 36px; }
  .intro { margin-top: 15px; font-size: 12.4px; line-height: 17px; width: 575px; }

  .offer { position: absolute; left: 149px; width: 302px; font-size: 11.5px; line-height: 17px; }
  .offer dl { display: grid; grid-template-columns: 109px 80px; }
  .offer dt { font-weight: 700; color: var(--label); }
  .offer dd { text-align: left; }
  .offer .total { position: absolute; right: 0; font-size: 16px; color: var(--ink-purple); }

  .floorplan {
    position: absolute; left: 786px; top: 387px; width: 266px; height: 213px;
    background: linear-gradient(135deg, #b7b7b3, #c2bfb6 50%, #adadaa); border: 2px solid #efe8da;
  }
  .download {
    position: absolute; left: 788px; top: 614px; width: 264px; height: 35px; display: flex; text-decoration: none;
  }
  .download-label {
    width: 228px; height: 35px; line-height: 35px; padding-left: 15px; color: var(--white); font-size: 11.5px;
    background: linear-gradient(var(--brand-red), #b8031f);
  }
  .download-label b { font-weight: 700; }
  .download-arrow {
    margin-left: 2px; width: 34px; height: 35px; display: flex; align-items: center; justify-content: center;
    background: linear-gradient(var(--brand-red), #b8031f);
  }

  .site-footer {
    position: absolute; left: 0; top: 786px; width: 1200px; height: 37px; background: var(--brand-red);
    color: var(--white); font-size: 11px;
  }
  .footer-links { position: absolute; left: 149px; top: 11px; }
  .footer-links a { color: var(--white); text-decoration: none; }
  .footer-links .sep { margin: 0 11px; }
  .copyright { position: absolute; right: 148px; top: 11px; }
</style>
</head>
<body>
  <div class="mascot" role="img" aria-label="Illustration: Maskottchen mit Brille und Krawatte, auf Büchern liegend"></div>
  <div class="site-name">weitblick-raeume.ch</div>

  <div class="nav-band"></div>
  <nav class="main-nav">
    <a href="#" style="left:601px">HOME</a>
    <a href="#" class="is-active" style="left:685px">FLÄCHEN</a>
    <a href="#" style="left:771px">BILDER</a>
    <a href="#" style="left:847px">LAGE</a>
    <a href="#" style="left:930px">KONTAKT</a>
  </nav>

  <div class="hero-photo" role="img" aria-label="Foto: helles Grossraumbüro mit grünen Stühlen und Schreibtischen"></div>
  <div class="hero-fade"></div>

  <main class="content">
    <h1 class="page-title">Flächen</h1>
    <p class="intro">Lorem ipsum dolor sit amet, consetetur sadipscing elitr, sed diam nonumy eirmod tempor invidunt ut labore et dolore magna aliquyam erat, sed diam voluptua. At vero eos et accusam et justo duo dolores et ea rebum. Stet clita kasd gubergren, no sea takimata sanctus est Lorem ipsum dolor sit amet. Lorem ipsum dolor sit amet, consetetur sadipscing elitr, sed diam nonumy eirmod tempor invidunt ut labore et dolore magn.</p>
  </main>

  <section class="offer" style="top:540px">
    <dl>
      <dt>Fläche:</dt><dd>1800 m²</dd>
      <dt>Miete / Monat:</dt><dd>2000,00&nbsp; CF</dd>
      <dt>Nebenkosten:</dt><dd>&nbsp;&nbsp;500,00&nbsp; CF</dd>
    </dl>
    <span class="total" style="top:21px">2500,00 CF</span>
  </section>

  <section class="offer" style="top:614px">
    <dl>
      <dt>Fläche:</dt><dd>900 m²</dd>
      <dt>Miete / Monat:</dt><dd>1200,00&nbsp; CF</dd>
      <dt>Nebenkosten:</dt><dd>&nbsp;&nbsp;400,00&nbsp; CF</dd>
    </dl>
    <span class="total" style="top:30px">1600,00 CF</span>
  </section>

  <section class="offer" style="top:690px">
    <dl>
      <dt>Fläche:</dt><dd>300 m²</dd>
      <dt>Miete / Monat:</dt><dd>500,00&nbsp; CF</dd>
      <dt>Nebenkosten:</dt><dd>&nbsp;&nbsp;&nbsp;300,00&nbsp; CF</dd>
    </dl>
    <span class="total" style="top:30px">800,00 CF</span>
  </section>

  <div class="floorplan" role="img" aria-label="Grundriss der Bürofläche mit Arbeitsplätzen"></div>
  <a class="download" href="#">
    <span class="download-label">Grundriss als <b>PDF</b> herunterladen</span>
    <span class="download-arrow">
      <svg width="14" height="14" viewBox="0 0 14 14" aria-hidden="true"><path d="M4 2 L10 7 L4 12" fill="none" stroke="#fff" stroke-width="3"/></svg>
    </span>
  </a>

  <footer class="site-footer">
    <div class="footer-links"><a href="#">Kontakt</a><span class="sep">|</span><a href="#">Impressum</a></div>
    <div class="copyright">© 2015 weitblick-raeume.ch</div>
  </footer>
</body>
</html>
```